Bright Fern Landscape Services LLC
business cards, letterhead, and envelopes.
Bright Fern Landscape Services LLC -
Creative Brief
Simple
Lydia Harcourt
Owner
2187 NW 58th Ave. Ocala, Fl 34475
lharcourt@quillmesh.net
Would like to use my tagline somewhere not necessarily right under the logo.

```html
<!DOCTYPE html>
<html lang="en">
<head>
<meta charset="utf-8">
<title>Bright Fern Landscape Services LLC – Business Cards</title>
<link rel="stylesheet" href="https://fonts.googleapis.com/css2?family=Open+Sans:wght@400;600;700&display=swap">
<style>
  :root {
    --backdrop: #e9eaeb;
    --card: #ffffff;
    --green: #1f8a3b;
    --green-dark: #176b2e;
    --green-light: #4cb862;
    --orange: #f08a1c;
    --ink: #4a4a4a;
    --rule: #bdbdbd;
  }
  * { margin: 0; padding: 0; box-sizing: border-box; }
  html, body { width: 1200px; height: 799px; overflow: hidden; }
  body {
    background: var(--backdrop);
    font-family: "Open Sans", Arial, sans-serif;
    position: relative;
  }
  .card {
    position: absolute;
    width: 520px;
    height: 300px;
    background: var(--card);
    border-radius: 22px;
    box-shadow: 0 6px 18px rgba(0,0,0,0.18);
    overflow: hidden;
  }
  .card--front { left: 70px; top: 100px; }
  .card--back { left: 610px; top: 400px; }

  .edge-tab {
    position: absolute;
    width: 9px;
    height: 60px;
    background: linear-gradient(180deg, var(--green-light), var(--green-dark));
    border-radius: 3px;
  }
  .card--front .edge-tab { left: 0; bottom: 70px; }
  .card--back .edge-tab { right: 0; top: 40px; }

  .person-name { color: var(--green); font-weight: 700; font-size: 19px; }
  .person-role { color: var(--orange); font-size: 12px; margin-top: 2px; }

  .brand { display: flex; align-items: center; gap: 10px; }
  .brand-dot { width: 26px; height: 26px; border-radius: 50%; background: var(--orange); flex: none; }
  .brand-name {
    color: var(--green);
    font-weight: 700;
    font-size: 22px;
    line-height: 1.1;
    width: 210px;
  }

  .contact { color: var(--ink); font-size: 12px; line-height: 1.55; }
  .contact-row { display: flex; align-items: center; gap: 7px; }
  .contact-row svg { width: 12px; height: 12px; flex: none; }

  .tagline {
    color: var(--green);
    font-size: 10.5px;
    font-weight: 600;
    letter-spacing: 0.4px;
    text-transform: uppercase;
  }

  /* front */
  .card--front .identity { position: absolute; left: 36px; top: 48px; }
  .card--front .brand { position: absolute; right: 30px; top: 60px; }
  .card--front .contact { position: absolute; left: 36px; top: 168px; }
  .card--front .tagline { position: absolute; left: 36px; bottom: 34px; }

  /* back */
  .card--back .brand { position: absolute; left: 150px; top: 50px; }
  .card--back .identity { position: absolute; left: 40px; top: 180px; }
  .card--back .divider {
    position: absolute; left: 232px; top: 160px;
    width: 1px; height: 80px; background: var(--rule);
  }
  .card--back .contact { position: absolute; left: 250px; top: 158px; }
  .card--back .tagline { position: absolute; left: 0; right: 0; bottom: 26px; text-align: center; }
</style>
</head>
<body>

<svg width="0" height="0" style="position:absolute" aria-hidden="true">
  <defs>
    <symbol id="icon-phone" viewBox="0 0 24 24">
      <path fill="#1f8a3b" d="M6.6 10.8a15.1 15.1 0 0 0 6.6 6.6l2.2-2.2a1 1 0 0 1 1-.25 11.4 11.4 0 0 0 3.6.57 1 1 0 0 1 1 1V20a1 1 0 0 1-1 1A17 17 0 0 1 3 4a1 1 0 0 1 1-1h3.5a1 1 0 0 1 1 1c0 1.250.2 2.45.57 3.57a1 1 0 0 1-.25 1z"/>
    </symbol>
    <symbol id="icon-mail" viewBox="0 0 24 24">
      <circle cx="12" cy="12" r="12" fill="#1f8a3b"/>
      <rect x="6" y="8" width="12" height="8" rx="1" fill="#fff"/>
      <path d="M6.5 8.5 12 12.5l5.5-4" fill="none" stroke="#1f8a3b" stroke-width="1.3"/>
    </symbol>
  </defs>
</svg>

<section class="card card--front">
  <div class="edge-tab"></div>
  <div class="identity">
    <div class="person-name">Lydia Harcourt</div>
    <div class="person-role">Owner</div>
  </div>
  <div class="brand">
    <span class="brand-dot"></span>
    <span class="brand-name">Bright Fern Landscape Services LLC</span>
  </div>
  <div class="contact">
    <div>2187 NW 58th Ave.</div>
    <div>Ocala, Fl 34475</div>
    <div class="contact-row"><svg><use href="#icon-phone"/></svg>(555) 014-2876</div>
    <div class="contact-row"><svg><use href="#icon-mail"/></svg>lharcourt@quillmesh.net</div>
  </div>
  <div class="tagline">Tending every yard with steady, lasting care</div>
</section>

<section class="card card--back">
  <div class="edge-tab"></div>
  <div class="brand">
    <span class="brand-dot"></span>
    <span class="brand-name">Bright Fern Landscape Services LLC</span>
  </div>
  <div class="identity">
    <div class="person-name">Lydia Harcourt</div>
    <div class="person-role">Owner</div>
  </div>
  <div class="divider"></div>
  <div class="contact">
    <div>2187 NW 58th Ave.</div>
    <div>Ocala, Fl 34475</div>
    <div class="contact-row"><svg><use href="#icon-phone"/></svg>(555) 014-2876</div>
    <div class="contact-row"><svg><use href="#icon-mail"/></svg>lharcourt@quillmesh.net</div>
  </div>
  <div class="tagline">Tending every yard with steady, lasting care</div>
</section>

</body>
</html>
```